Lantrn & Ladle Festival poster,rack card, business card

We need phase 1 of the 1st annual Lantern & Ladle Festival to be held June 12 &13 2015. Location and etc to be given upon completion. We need a Poster design for store windows, a rack card for rack display, and a business size card to hand out to prospective exhibitors and attendees. The festival will focus on Food trucks and food vendors, along with multiple bands to play throughout the event . Additional work will be asked for after the phase one is complete, and we have more info such as sponsors and bands.

Attn all designers...... I opologize for the extreme delay on the project. I had an incendent that landed me in the hospital on sept 7, and I will not be released until next week ,at which time we will come to a decision. Thanks for your patience. Milo

```html
<!DOCTYPE html>
<html lang="en">
<head>
<meta charset="utf-8">
<title>Lantern &amp; Ladle Festival Poster</title>
<link rel="stylesheet" href="https://fonts.googleapis.com/css2?family=Great+Vibes&family=Arimo&display=swap">
<style>
  :root {
    --red-deep: #a20a0a;
    --red-warm: #cf3a0c;
    --band-pale: #fdf6b8;
    --band-gold: #f4d21c;
    --gold-light: #fff27a;
    --gold-dark: #e0a21c;
    --title-shadow: #5a1400;
    --white: #ffffff;
    --wood-light: #7a4a28;
    --wood-dark: #3b1e0f;
    --roast-light: #e3a24e;
    --roast-dark: #9a4f1a;
  }
  * { margin: 0; padding: 0; box-sizing: border-box; }
  html, body { width: 776px; height: 1200px; overflow: hidden; background: var(--white); }
  .poster {
    position: relative;
    width: 776px;
    height: 1200px;
    overflow: hidden;
    background: var(--white);
  }
  .red-panel {
    position: absolute;
    left: 0; top: 0;
    width: 469px; height: 1200px;
    background: linear-gradient(to bottom, var(--red-deep) 0%, var(--red-warm) 50%, var(--red-deep) 100%);
  }
  .gold-band {
    position: absolute;
    left: 469px; top: 0;
    width: 24px; height: 1200px;
    background: linear-gradient(to bottom, var(--band-pale) 0%, var(--band-gold) 45%, var(--band-gold) 100%);
  }
  .violin-photo {
    position: absolute;
    left: 493px; top: 147px;
    width: 283px; height: 900px;
    background: radial-gradient(ellipse at 55% 55%, var(--wood-light) 0%, var(--wood-dark) 85%);
    border-radius: 120px 0 0 60px;
  }
  .roast-photo {
    position: absolute;
    left: 405px; top: 880px;
    width: 371px; height: 227px;
    background: radial-gradient(ellipse at 50% 45%, var(--roast-light) 0%, var(--roast-dark) 90%);
    border-radius: 50% 0 0 50%;
  }
  .title {
    position: absolute;
    left: 0; top: 0;
    font-family: "Great Vibes", cursive;
    color: var(--gold-light);
    text-shadow: 2px 3px 2px var(--title-shadow);
    line-height: 1;
  }
  .title-word {
    position: absolute;
    white-space: nowrap;
    font-size: 118px;
    background: linear-gradient(to bottom, var(--gold-light) 20%, var(--gold-dark) 95%);
    -webkit-background-clip: text;
    background-clip: text;
    color: transparent;
    filter: drop-shadow(2px 3px 1px var(--title-shadow));
  }
  .title-first { left: 14px; top: 450px; }
  .title-amp {
    position: absolute;
    left: 268px; top: 572px;
    font-size: 60px;
    color: var(--gold-dark);
    font-family: "Arimo", sans-serif;
    font-weight: 400;
  }
  .title-second { left: 240px; top: 610px; }
  .dates {
    position: absolute;
    left: 16px; top: 775px;
    font-family: "Arimo", sans-serif;
    font-size: 37px;
    color: var(--white);
    white-space: nowrap;
  }
</style>
</head>
<body>
  <main class="poster">
    <div class="red-panel"></div>
    <div class="gold-band"></div>
    <div class="violin-photo" role="img" aria-label="Photograph of an aged wooden violin standing upright"></div>
    <div class="roast-photo" role="img" aria-label="Photograph of a roast turkey on a platter with vegetables, oranges and herbs"></div>
    <h1 class="title">
      <span class="title-word title-first">Lantern</span>
      <span class="title-amp">&amp;</span>
      <span class="title-word title-second">Ladle</span>
    </h1>
    <p class="dates">June 12 &amp; 13, 2015.</p>
  </main>
</body>
</html>
```